Flyer-Design für Abschleppunternehmen
Zielgruppe
Wir sind ein Abschleppunternehmen und sind bestrebt neue Kunden zu gewinnen. Vor allem im Bereich 'Falschparker' suchen wir Firmen/Unternehmen mit Privatparkplätzen, die von fremden Personen zu geparkt werden. Hierzu ist stark darauf hinzuweisen, dass diese Leistung für den Autraggeber völlig kostenlos und ohne Aufwand anzufordern ist.
Aufgabenstellung
Vorschlag DIN Fyler 21x9,8cm . Wir sind ein 24/7 Betrieb. Rufnr. 073845190. Es ist darauf hinzweisen, dass wir ein unternehmen aus der direkten umgebung sind.

```html
<!DOCTYPE html>
<html lang="de">
<head>
<meta charset="utf-8">
<title>Krunzel Abschleppdienst – Flyer</title>
<link href="https://fonts.googleapis.com/css2?family=Roboto:wght@400;500;700;900&family=Roboto+Condensed:wght@700&display=swap" rel="stylesheet">
<style>
  :root {
    --yellow: #ffd200;
    --red: #d90000;
    --black: #111111;
    --ink: #1a1a1a;
    --white: #ffffff;
    --photo-warm: #c9b25a;
    --photo-grey: #9a9a95;
  }
  * { box-sizing: border-box; margin: 0; padding: 0; }
  html, body { width: 1200px; height: 973px; overflow: hidden; background: var(--white); }
  body { position: relative; font-family: "Roboto", sans-serif; color: var(--ink); }

  .panel {
    position: absolute; top: 56px; width: 402px; height: 862px;
    background: var(--white);
    box-shadow: 0 2px 12px rgba(0,0,0,0.14);
    overflow: hidden;
  }
  .panel--front { left: 182px; }
  .panel--back { left: 634px; top: 57px; }

  /* Brand */
  .brand { position: absolute; left: 34px; top: 108px; display: flex; align-items: center; gap: 8px; }
  .brand__dot { width: 16px; height: 16px; background: var(--red); border-radius: 50%; }
  .brand__name { font-weight: 900; font-size: 26px; color: var(--red); letter-spacing: 0.5px; }
  .no-stop-sign { position: absolute; left: 298px; top: 42px; width: 64px; height: 64px; }

  /* Hero */
  .hero-box { position: absolute; left: 11px; top: 149px; width: 380px; height: 112px; background: var(--yellow); padding: 20px 0 0 27px; }
  .hero-box__title { font-weight: 700; font-size: 33px; line-height: 1.1; color: var(--black); }
  .hero-box__sub { font-size: 22px; margin-top: 6px; color: var(--black); }
  .hero-photo { position: absolute; left: 11px; top: 261px; width: 380px; height: 244px;
    background: linear-gradient(160deg, #8e8e88 0%, #b5b3a6 40%, #d8bf3a 62%, #7b7a74 100%); }
  .years-badge { position: absolute; left: 36px; top: 433px; width: 128px; height: 128px; border-radius: 50%;
    background: var(--black); color: var(--white); text-align: center; padding-top: 34px; line-height: 1; }
  .years-badge__seit { font-size: 26px; }
  .years-badge__num { font-size: 36px; font-weight: 700; }
  .years-badge__jahren { font-size: 26px; display: block; margin-top: 6px; padding-left: 10px; }

  /* Marker headings */
  .marker { font-family: "Roboto Condensed", sans-serif; font-weight: 700; color: var(--black); position: relative; }
  .marker__line { position: relative; display: inline-block; padding: 0 10px; }
  .marker__line::before { content: ""; position: absolute; left: 0; right: 0; bottom: 2px; height: 45%; background: var(--yellow); z-index: 0; }
  .marker__text { position: relative; z-index: 1; }

  .region-heading { position: absolute; left: 27px; top: 592px; font-size: 23px; line-height: 29px; }
  .region-heading .marker__line { display: block; width: fit-content; }
  .body-copy { position: absolute; left: 37px; top: 664px; font-size: 19px; line-height: 23px; }
  .body-copy strong { font-weight: 700; }
  .call-note { position: absolute; left: 37px; top: 725px; font-size: 19px; font-weight: 700; }

  /* Footer */
  .call-bar { position: absolute; left: 0; bottom: 0; width: 100%; height: 71px; background: var(--red); color: var(--white);
    display: flex; align-items: center; }
  .call-bar__phone { position: absolute; left: 48px; top: 22px; width: 30px; height: 30px; }
  .call-bar__number { position: absolute; left: 0; right: 0; text-align: center; font-size: 25px; font-weight: 700; letter-spacing: 0.5px; }
  .call-bar__service { position: absolute; right: 38px; top: 16px; width: 40px; height: 40px; }

  /* Back panel */
  .services-heading { position: absolute; left: 22px; top: 62px; font-size: 29px; line-height: 36px; }
  .services-heading .marker__line { padding: 0 16px; }
  .services-heading .marker__line::before { height: 36%; bottom: 0; }
  .service-list { position: absolute; left: 37px; top: 133px; list-style: none; }
  .service-list li { height: 42px; font-size: 20px; display: flex; align-items: center; letter-spacing: 0.2px; }
  .service-list li::before { content: "\2731"; font-size: 15px; width: 29px; color: var(--black); }

  .gallery { position: absolute; }
  .gallery--garage { left: 0; top: 418px; width: 156px; height: 186px; background: linear-gradient(180deg, #c9ccd0 0%, #b7b19a 45%, #a6a39b 100%); }
  .gallery--deck { left: 165px; top: 418px; width: 237px; height: 186px; background: linear-gradient(170deg, #a9a39c 0%, #7d7c7e 45%, #c9b337 65%, #8a8a88 100%); }
  .gallery--yard { left: 0; top: 615px; width: 402px; height: 167px; background: linear-gradient(180deg, #d9d4cc 0%, #c69048 40%, #d3b33c 65%, #5a5a5c 100%); }
</style>
</head>
<body>

<section class="panel panel--front">
  <div class="brand"><span class="brand__dot"></span><span class="brand__name">Krunzel</span></div>
  <svg class="no-stop-sign" viewBox="0 0 64 64" aria-label="Halteverbot-Schild">
    <circle cx="32" cy="32" r="30" fill="#d90000"/>
    <circle cx="32" cy="32" r="24" fill="#1a9ee0"/>
    <path d="M15 15 L49 49 M49 15 L15 49" stroke="#d90000" stroke-width="6"/>
  </svg>

  <div class="hero-box">
    <h1 class="hero-box__title">Falschparker?</h1>
    <p class="hero-box__sub">Wir erledigen das für Sie!</p>
  </div>
  <div class="hero-photo" role="img" aria-label="Gelber Abschlepp-Pickup neben einem weißen Auto in einem Parkhaus"></div>
  <div class="years-badge">
    <span class="years-badge__seit">Seit </span><span class="years-badge__num">50</span>
    <span class="years-badge__jahren">Jahren</span>
  </div>

  <h2 class="marker region-heading">
    <span class="marker__line"><span class="marker__text">Wir sind Ihr Abschleppdienst</span></span>
    <span class="marker__line"><span class="marker__text">der Region.</span></span>
  </h2>
  <p class="body-copy">Lassen Sie unberechtigt geparkte<br>Fahrzeuge <strong>kostenlos</strong> abschleppen!</p>
  <p class="call-note">Ein Anruf genügt.</p>

  <footer class="call-bar">
    <svg class="call-bar__phone" viewBox="0 0 24 24" aria-hidden="true"><path d="M5 3 L9 3 L10.5 7.5 L8 9.5 C9.2 12.3 11.7 14.8 14.5 16 L16.5 13.5 L21 15 L21 19 C21 20 20 21 19 21 C10.5 20.5 3.5 13.5 3 5 C3 4 4 3 5 3 Z" fill="none" stroke="#fff" stroke-width="1.6" stroke-linejoin="round"/></svg>
    <span class="call-bar__number">+49 7384 5190</span>
    <svg class="call-bar__service" viewBox="0 0 40 40" aria-label="24/7 Service">
      <path d="M33 9 A17 17 0 1 0 37 20" fill="none" stroke="#fff" stroke-width="2"/>
      <path d="M30 4 L34 9 L28 11" fill="none" stroke="#fff" stroke-width="2"/>
      <text x="19" y="20" text-anchor="middle" font-family="Roboto, sans-serif" font-weight="700" font-size="9" fill="#fff">24/7</text>
      <text x="19" y="27" text-anchor="middle" font-family="Roboto, sans-serif" font-weight="700" font-size="5" fill="#fff">SERVICE</text>
    </svg>
  </footer>
</section>

<section class="panel panel--back">
  <h2 class="marker services-heading"><span class="marker__line"><span class="marker__text">Wir können auch mehr!</span></span></h2>
  <ul class="service-list">
    <li>PKW Abschlepp- Bergungsdienst</li>
    <li>LKW Abschlepp- Bergungsdienst</li>
    <li>Kranservice</li>
    <li>Fahrzeugtransporte</li>
    <li>Ölspurbeseitigung</li>
    <li>Fahrzeugöffnungen</li>
  </ul>
  <div class="gallery gallery--garage" role="img" aria-label="Gelber Pickup in einer Tiefgarageneinfahrt"></div>
  <div class="gallery gallery--deck" role="img" aria-label="Gelber Pickup auf einem Parkdeck"></div>
  <div class="gallery gallery--yard" role="img" aria-label="Großer gelber Abschlepp-LKW auf dem Firmenhof im Herbst"></div>

  <footer class="call-bar">
    <svg class="call-bar__phone" viewBox="0 0 24 24" aria-hidden="true"><path d="M5 3 L9 3 L10.5 7.5 L8 9.5 C9.2 12.3 11.7 14.8 14.5 16 L16.5 13.5 L21 15 L21 19 C21 20 20 21 19 21 C10.5 20.5 3.5 13.5 3 5 C3 4 4 3 5 3 Z" fill="none" stroke="#fff" stroke-width="1.6" stroke-linejoin="round"/></svg>
    <span class="call-bar__number">+49 7384 5190</span>
    <svg class="call-bar__service" viewBox="0 0 40 40" aria-label="24/7 Service">
      <path d="M33 9 A17 17 0 1 0 37 20" fill="none" stroke="#fff" stroke-width="2"/>
      <path d="M30 4 L34 9 L28 11" fill="none" stroke="#fff" stroke-width="2"/>
      <text x="19" y="20" text-anchor="middle" font-family="Roboto, sans-serif" font-weight="700" font-size="9" fill="#fff">24/7</text>
      <text x="19" y="27" text-anchor="middle" font-family="Roboto, sans-serif" font-weight="700" font-size="5" fill="#fff">SERVICE</text>
    </svg>
  </footer>
</section>

</body>
</html>
```